Business Card Design

i am looking a business card for a car rental company long with Taxi service also a logo.

what is the latest with my project

Industry/Entity Type

Business

Contact Information for Business Card

name of the Company is Kestrel Bay Motor Leasing and Taxi Services
Address: Pelican Row Village, St. Aldric's Parish Antigua
Tele# 555-0142/5550187-555-0163
Email: lorimbeck@quillmarsh.test

Font styles to use
Script

```html
<!DOCTYPE html>
<html lang="en">
<head>
<meta charset="utf-8">
<title>Kestrel Bay Motor Leasing and Taxi Services — Business Card</title>
<link rel="stylesheet" href="https://fonts.googleapis.com/css2?family=Courgette&family=Tinos&display=swap">
<style>
  :root {
    --paper: #ffffff;
    --sea: #00ffff;
    --rule: #9a9a9a;
    --ink: #000000;
    --contact: #e6e6e6;
  }
  html, body {
    margin: 0;
    padding: 0;
    overflow: hidden;
    background: var(--paper);
  }
  .card {
    position: relative;
    width: 1200px;
    height: 733px;
    overflow: hidden;
    background: var(--paper);
  }
  .card__wave {
    position: absolute;
    inset: 0;
    width: 1200px;
    height: 733px;
  }
  .card__wave-fill { fill: var(--sea); }
  .card__wave-line { fill: none; stroke: var(--rule); stroke-width: 6; }
  .card__mark {
    position: absolute;
    left: 293px;
    top: 41px;
    width: 654px;
    height: 203px;
    background: var(--ink);
    border-radius: 90px 110px 40px 40px;
  }
  .card__name {
    position: absolute;
    left: 0;
    width: 1200px;
    top: 262px;
    margin: 0;
    text-align: center;
    font-family: "Courgette", cursive;
    font-weight: 400;
    font-size: 38px;
    color: var(--ink);
    white-space: nowrap;
  }
  .card__contact {
    position: absolute;
    left: 38px;
    top: 570px;
    margin: 0;
    padding: 0;
    list-style: none;
    font-family: "Tinos", serif;
    font-size: 27px;
    line-height: 38.5px;
    color: var(--contact);
  }
</style>
</head>
<body>
  <main class="card">
    <svg class="card__wave" viewBox="0 0 1200 733" aria-hidden="true">
      <path class="card__wave-fill" d="M0,226 Q600,640 1200,237 L1200,733 L0,733 Z"/>
      <path class="card__wave-line" d="M0,226 Q600,640 1200,237"/>
    </svg>
    <div class="card__mark" role="img" aria-label="Company emblem: black vehicle silhouette"></div>
    <h1 class="card__name">Kestrel Bay Motor Leasing and Taxi Services</h1>
    <ul class="card__contact">
      <li>Address: Pelican Row Village, St. Aldric's Parish Antigua</li>
      <li>Tele # 555-0142/5550187-555-0163</li>
      <li>Email: lorimbeck@quillmarsh.test</li>
    </ul>
  </main>
</body>
</html>
```